Mobile phone signal boosting solutions needs a website

We need a website design for the reselling of a mobile signal boosting product set. These solutions are Travik exempt and will provide an indoor signal for mobile phones. We would like to see designs that incorporate the colours and feel of our logo. The domain will be
nestorbolt.com / co.uk
Overview of the company and how it is to be used: Nestor Bolt (domain name) will work with business and end user to provide mobile signal boosting – where people struggle indoors with a mobile signal our solutions will help by finding the smallest signal and boosting it, allowing users to use voice and data over their mobile network (please note this is not wireless signal boosting)
Number of Pages:
-Home
-Solutions / How it works
-Case Studies
-Contact
Text content: Currently just use placeholders
Technical specs : Wordpress and ability to use CMS if that’s relevant
Target Market(s)
Business professional all markets /high end residential
Coding
Coded - Design and coding required
Number of Pages Required
4 page
Look and feel

```html
<!DOCTYPE html>
<html lang="en">
<head>
<meta charset="utf-8">
<title>Nestor Bolt – Mobile Signal Booster</title>
<link rel="stylesheet" href="https://fonts.googleapis.com/css2?family=Oswald:wght@500;600;700&family=Roboto:wght@400;500;700&display=swap">
<style>
:root{
  --yellow:#fcc200;
  --yellow-dark:#e9a900;
  --black:#000;
  --ink:#111;
  --text:#777;
  --grey-bg:#f4f4f4;
  --white:#fff;
}
*{box-sizing:border-box;margin:0;padding:0}
html,body{width:1200px;height:3686px;overflow:hidden}
body{position:relative;font-family:Roboto,Arial,sans-serif;color:var(--ink);background:var(--white)}
.abs{position:absolute}
a{color:inherit;text-decoration:none}

/* top bar */
.topbar{left:0;top:0;width:1200px;height:46px;background:var(--black);color:var(--white);font-size:14px}
.topbar .item{position:absolute;top:14px;display:flex;align-items:center;gap:10px}
.social{display:flex;gap:6px}
.social span{width:32px;height:32px;border:1.5px solid currentColor;border-radius:50%;display:block}
.topbar .social{position:absolute;right:111px;top:7px}

/* nav */
.nav{left:0;top:46px;width:1200px;height:79px;background:var(--white);font-size:15px;font-weight:500;text-transform:uppercase}
.nav a{position:absolute;top:0;height:79px;line-height:79px;padding:0 20px}
.nav .active{color:var(--yellow)}
.nav .sep{position:absolute;top:0;width:1px;height:79px;background:#eee}
.quote{background:var(--yellow);font-weight:700}
.brand-box{left:506px;top:0;width:188px;height:198px;z-index:5;filter:drop-shadow(0 3px 6px rgba(0,0,0,.18))}
.brand{position:absolute;top:60px;width:188px;text-align:center}
.brand .mark{display:inline-block;width:14px;height:14px;background:var(--yellow);margin-bottom:10px}
.brand .name{font-size:25px;font-weight:500;letter-spacing:-.5px;color:var(--ink)}
.brand .tag{font-size:10px;color:var(--yellow);font-weight:500;letter-spacing:.3px}

/* hero */
.hero{left:0;top:125px;width:1200px;height:662px}
.hero-text{left:0;top:340px;width:1200px;text-align:center}
h1{font-family:Oswald,sans-serif;font-size:42px;font-weight:600;color:var(--ink)}
.hero-text p{font-size:17px;line-height:27px;width:470px;margin:22px auto 0;color:#222;font-weight:500}
.btn{display:inline-block;background:var(--yellow);font-weight:700;font-size:14px;text-transform:uppercase;color:var(--ink)}
.hero-text .btn{margin-top:34px;width:136px;height:46px;line-height:46px}
.dots{left:565px;top:706px;display:flex;gap:8px}
.dots span{width:10px;height:10px;border:1.5px solid #fff;border-radius:50%}
.dots .on{background:#fff}
.arrow{width:28px;height:52px;background:var(--white);top:368px}

/* headings */
.h2{font-family:Oswald,sans-serif;font-size:41px;font-weight:600;text-transform:uppercase;color:var(--ink)}
.center-title{left:0;width:1200px;text-align:center}
.center-title .rule{display:block;width:56px;height:3px;background:var(--yellow);margin:6px auto 0}

/* about */
.about-copy{left:661px;top:912px;width:427px}
.about-copy .h2{display:flex;align-items:center;gap:14px}
.about-copy .h2::after{content:"";width:56px;height:3px;background:var(--yellow)}
.about-copy p{font-size:14px;line-height:25.7px;color:var(--text);text-align:justify;margin-top:24px}
.about-copy p+p{margin-top:14px}
.btn-outline{display:inline-block;margin-top:36px;width:137px;height:49px;line-height:45px;text-align:center;border:2px solid var(--yellow);font-weight:700;font-size:15px;text-transform:uppercase}

/* solutions */
.solutions{left:0;top:1472px;width:1200px;height:616px;background:var(--grey-bg)}
.card{position:absolute;top:1632px;width:314px;height:387px;background:var(--white);box-shadow:0 2px 8px rgba(0,0,0,.08)}
.card .pic{height:209px}
.card .icon{position:absolute;left:16px;top:173px;width:71px;height:71px;background:var(--yellow);border:2px solid #fff;display:flex;align-items:center;justify-content:center}
.card h3{position:absolute;left:106px;top:226px;font-size:16px;font-weight:500;text-transform:uppercase}
.card p{position:absolute;left:16px;top:266px;width:284px;font-size:14px;line-height:25px;color:var(--text)}
.card .more{position:absolute;left:16px;top:348px;font-size:13px;font-weight:700;color:var(--yellow);text-transform:uppercase}

/* case studies */
.case{position:absolute;top:2287px;width:232px}
.case h4{font-size:15px;font-weight:500;line-height:22px;margin-top:17px}
.case .date{display:flex;align-items:center;gap:10px;font-size:13px;color:var(--text);margin-top:8px}
.case .date i{width:13px;height:12px;background:#f4d27a;display:block}

/* contact */
.touch{left:0;top:2749px;width:1200px;height:620px;background:radial-gradient(ellipse at 30% 70%,#f9d34a 0%,#f4c000 45%,#e2ad00 100%)}
.touch .h2{color:var(--white)}
.touch .rule{background:var(--white)}
.field{position:absolute;background:var(--white);border-radius:2px;font-size:14px;color:#888;padding:0 17px;line-height:49px}
.send{left:511px;top:3076px;width:178px;height:49px;line-height:49px;text-align:center;background:var(--black);color:var(--white)}

/* footer */
.footer{left:0;top:3179px;width:1200px;height:507px}
.foot-brand{left:111px;top:3418px;width:140px;text-align:center;color:var(--white)}
.foot-brand .name{color:var(--white)}
.vline{position:absolute;top:3346px;width:2px;height:258px;background:#fff;opacity:.85}
.fcol{position:absolute;top:3370px;color:var(--white)}
.fcol h5{font-size:17px;font-weight:700;text-transform:uppercase;margin-bottom:22px}
.fcol ul{list-style:none;font-size:14px}
.fcol li{display:flex;gap:22px;height:44px;align-items:flex-start}
.fcol li b{color:var(--yellow);font-weight:700}
.info{display:flex;gap:18px;margin-bottom:18px}
.info .ic{width:12px;height:12px;background:var(--yellow);border-radius:2px;margin-top:3px}
.info strong{display:block;font-size:14px;font-weight:500;margin-bottom:6px}
.info span{font-size:12px;line-height:18px}
.news{left:805px;top:3415px;width:283px;height:46px;background:var(--white);border:3px solid var(--yellow)}
.news span{position:absolute;left:16px;top:12px;font-size:14px;color:#888}
.news b{position:absolute;right:0;top:0;width:103px;height:40px;background:var(--yellow);line-height:40px;text-align:center;font-size:14px}
.fsocial{left:805px;top:3484px;color:var(--white)}
.fsocial span{width:38px;height:38px}
.fsocial span:first-child{background:var(--yellow);border-color:var(--yellow)}
.bottom-rule{left:111px;top:3620px;width:977px;height:1px;background:#555}
.copy{left:0;top:3646px;width:1200px;text-align:center;color:var(--white);font-size:13px}
.chat{left:1116px;top:3576px;width:44px;height:44px;border-radius:50%;background:var(--yellow);display:flex;align-items:center;justify-content:center}
</style>
</head>
<body>

<!-- Top bar -->
<div class="abs topbar">
  <div class="item" style="left:111px">
    <svg width="13" height="13" viewBox="0 0 24 24"><path fill="#fcc200" d="M6.6 10.8a15.1 15.1 0 006.6 6.6l2.2-2.2c.3-.3.7-.4 1-.2 1.1.4 2.3.6 3.6.6.6 0 1 .4 1 1V20c0 .6-.4 1-1 1A17 17 0 013 4c0-.6.4-1 1-1h3.5c.6 0 1 .4 1 1 0 1.3.2 2.5.6 3.6.1.3 0 .7-.2 1z"/></svg>
    +1 (888) 888 8888
  </div>
  <div class="item" style="left:274px">
    <svg width="14" height="11" viewBox="0 0 14 11"><rect width="14" height="11" rx="1" fill="#fcc200"/><path d="M0 1l7 5 7-5" stroke="#000" fill="none"/></svg>
    info@nestorbolt.com
  </div>
  <div class="social"><span></span><span></span><span></span></div>
</div>

<!-- Navigation -->
<nav class="abs nav">
  <a class="active" style="left:91px">Home</a>
  <div class="sep" style="left:174px"></div>
  <a style="left:173px">Solutions</a>
  <div class="sep" style="left:296px"></div>
  <a style="left:294px">Case Studies</a>
  <a style="left:776px">Contact</a>
  <a class="quote" style="left:917px;width:171px;text-align:center;padding:0">Request a Quote</a>
</nav>

<div class="abs brand-box">
  <svg width="188" height="198" style="position:absolute;left:0;top:0"><polygon points="0,0 188,0 188,128 94,198 0,128" fill="#fff"/></svg>
  <div class="brand">
    <span class="mark"></span>
    <div class="name">Nestor Bolt</div>
    <div class="tag">MOBILE SIGNAL BOOSTER</div>
  </div>
</div>

<!-- Hero -->
<div class="abs hero">
  <svg width="1200" height="662">
    <defs>
      <linearGradient id="heroFill" x1="0" y1="0" x2="1" y2="1">
        <stop offset="0" stop-color="#d9d6d0"/>
        <stop offset=".45" stop-color="#ece9e4"/>
        <stop offset=".75" stop-color="#c9c3ba"/>
        <stop offset="1" stop-color="#6f6a63"/>
      </linearGradient>
    </defs>
    <polygon points="0,662 0,473 600,662 1200,473 1200,662" fill="#fff"/>
    <polygon points="0,473 600,662 1200,473 1200,488 600,662 0,488" fill="#fcc200"/>
    <polygon points="0,0 1200,0 1200,473 600,662 0,473" fill="#fcc200"/>
    <polygon role="img" aria-label="Photo of a network router with ethernet cables and a hand holding a phone" points="0,0 1200,0 1200,470 600,632 0,470" fill="url(#heroFill)"/>
  </svg>
</div>
<div class="abs arrow" style="left:0;clip-path:polygon(0 0,100% 50%,0 100%)"></div>
<div class="abs arrow" style="left:1172px;clip-path:polygon(100% 0,0 50%,100% 100%)"></div>
<div class="abs hero-text">
  <h1>NESTOR BOLT</h1>
  <p>Lorem ipsum dolor sit amet, consectetur adipiscing elit, sed do eiusmod tempor incididuntut.</p>
  <a class="btn">Get Started</a>
</div>
<div class="abs dots"><span></span><span class="on"></span><span></span><span></span></div>

<!-- About -->
<svg class="abs" style="left:111px;top:1035px" width="358" height="320">
  <path d="M70 6H6V314H352V266" fill="none" stroke="#fcc200" stroke-width="11"/>
</svg>
<div class="abs" role="img" aria-label="Photo of a network patch panel with blue cables" style="left:187px;top:875px;width:298px;height:334px;background:linear-gradient(160deg,#3a5fa8,#15213f 60%,#2d4f8f)"></div>
<div class="abs" role="img" aria-label="Photo of a hand holding a phone beside a coffee cup" style="left:343px;top:1038px;width:237px;height:263px;background:#fff;padding:7px"><div style="width:100%;height:100%;background:linear-gradient(180deg,#e6e3de,#cfcac3)"></div></div>
<div class="abs about-copy">
  <div class="h2">About Us</div>
  <p>Lorem ipsum dolor sit amet, consectetur adipiscing elit, sed do eiusmod tempor incididunt ut labore et dolore magna aliqua. Ut enim ad minim veniam, quis nostrud exercitation ullamco laboris nisi ut aliqudidunt ut laboripea.</p>
  <p>Sed um dolor sit amet, consectetur adipiscing elit, sed do eiusmod tempor incididunt ut labore et dolore magna aliqua. Ut enim ad minim veniam, quis nostrud exercitation ullamco laboris nisi ut aliquiis nostrud exercdolore magna aliquaitpea.</p>
  <a class="btn-outline">Learn More</a>
</div>

<!-- Solutions -->
<div class="abs solutions"></div>
<div class="abs center-title h2" style="top:1528px">Our Solutions<span class="rule"></span></div>

<div class="card" style="left:111px">
  <div class="pic" role="img" aria-label="Photo of a hand plugging an ethernet cable into a switch" style="background:linear-gradient(135deg,#d8c7b8,#3b3b3b 70%,#222)"></div>
  <div class="icon"><svg width="40" height="40" viewBox="0 0 40 40" fill="none" stroke="#111" stroke-width="2"><circle cx="20" cy="11" r="5"/><path d="M20 16v7M8 27v-4h24v4M20 23v4"/><rect x="3" y="27" width="9" height="7"/><rect x="15.5" y="27" width="9" height="7"/><rect x="28" y="27" width="9" height="7"/></svg></div>
  <h3>Lorem Ipsum Sed</h3>
  <p>Lorem ipsum dolor sit amet, consectetur a dipiscing elit, sed do eiusmod tempor incid idunt ut labore et dolorea.</p>
  <a class="more">Learn More &nbsp;»</a>
</div>
<div class="card" style="left:443px">
  <div class="pic" role="img" aria-label="Photo of a wireless router on a desk with a person and laptop" style="background:linear-gradient(160deg,#e7e5e0,#b9b4ab 60%,#3a3834)"></div>
  <div class="icon"><svg width="40" height="40" viewBox="0 0 40 40" fill="none" stroke="#111" stroke-width="2"><rect x="6" y="5" width="16" height="28" rx="2"/><circle cx="28" cy="14" r="7"/><path d="M21 14h14M28 7v14M10 24h8"/></svg></div>
  <h3>Lorem Ipsum Sed</h3>
  <p>Lorem ipsum dolor sit amet, consectetur a dipiscing elit, sed do eiusmod tempor incid idunt ut labore et dolorea.</p>
  <a class="more">Learn More &nbsp;»</a>
</div>
<div class="card" style="left:775px">
  <div class="pic" role="img" aria-label="Photo of blue ethernet cables plugged into a switch" style="background:linear-gradient(150deg,#c4603a,#2a4f9a 45%,#122a5c)"></div>
  <div class="icon"><svg width="40" height="40" viewBox="0 0 40 40" fill="none" stroke="#111" stroke-width="2"><circle cx="20" cy="17" r="3"/><path d="M20 20v14M14 11a8 8 0 000 12M26 11a8 8 0 010 12M9 6a15 15 0 000 22M31 6a15 15 0 010 22"/></svg></div>
  <h3>Lorem Ipsum Sed</h3>
  <p>Lorem ipsum dolor sit amet, consectetur a dipiscing elit, sed do eiusmod tempor incid idunt ut labore et dolorea.</p>
  <a class="more">Learn More &nbsp;»</a>
</div>

<!-- Case studies -->
<div class="abs center-title h2" style="top:2180px">Case Studies<span class="rule"></span></div>
<div class="case" style="left:111px">
  <div role="img" aria-label="Photo of network equipment with cables" style="height:214px;background:linear-gradient(150deg,#1e3e7a,#0c1630 60%,#3e6fa5)"></div>
  <h4>Sed ut perspiciatis unde omnis iste naiciatis undtus</h4>
  <div class="date"><i></i>31 Jan 2023</div>
</div>
<div class="case" style="left:359px">
  <div role="img" aria-label="Photo of two technicians in a server room" style="height:283px;background:linear-gradient(160deg,#2b3344,#8c97a6 50%,#1a1f28)"></div>
  <h4>Sed ut perspiciatis unde omnis iste naiciatis undtus</h4>
  <div class="date"><i></i>31 Jan 2023</div>
</div>
<div class="case" style="left:608px">
  <div role="img" aria-label="Photo of a router next to a laptop and phone" style="height:214px;background:linear-gradient(160deg,#e9e6e1,#b7aea2 55%,#6b5a46)"></div>
  <h4>Sed ut perspiciatis unde omnis iste naiciatis undtus</h4>
  <div class="date"><i></i>31 Jan 2023</div>
</div>
<div class="case" style="left:857px">
  <div role="img" aria-label="Photo of a white router on a table near a window" style="height:283px;background:linear-gradient(170deg,#6f8a4a,#c9cfc4 45%,#8a6a45)"></div>
  <h4>Sed ut perspiciatis unde omnis iste naiciatis undtus</h4>
  <div class="date"><i></i>31 Jan 2023</div>
</div>

<!-- Get in touch -->
<div class="abs touch"></div>
<div class="abs center-title h2" style="top:2802px;color:#fff">Get In Touch<span class="rule" style="background:#fff"></span></div>
<div class="field" style="left:165px;top:2903px;width:283px;height:49px">Full Name</div>
<div class="field" style="left:458px;top:2903px;width:283px;height:49px">Phone</div>
<div class="field" style="left:751px;top:2903px;width:283px;height:49px">Email Address</div>
<div class="field" style="left:165px;top:2965px;width:869px;height:93px;line-height:50px">Message</div>
<a class="abs btn send">Send Message</a>

<!-- Footer -->
<div class="abs footer">
  <svg width="1200" height="507">
    <polygon points="0,187 600,0 1200,187 1200,507 0,507" fill="#000"/>
    <polygon points="0,187 600,0 1200,187 1200,180 600,-8 0,180" fill="#fff"/>
  </svg>
</div>
<div class="abs foot-brand brand" style="left:111px;top:3415px;width:140px;text-align:left">
  <span class="mark"></span>
  <div class="name" style="color:#fff">Nestor Bolt</div>
  <div class="tag">MOBILE SIGNAL BOOSTER</div>
</div>
<div class="vline" style="left:325px"></div>
<div class="vline" style="left:538px"></div>
<div class="vline" style="left:778px"></div>

<div class="fcol" style="left:363px">
  <h5>Quick Links</h5>
  <ul>
    <li><b>»</b>Home</li>
    <li><b>»</b>Solutions</li>
    <li><b>»</b>Case Studies</li>
    <li><b>»</b>Contact</li>
  </ul>
</div>
<div class="fcol" style="left:573px">
  <h5>Contact Info</h5>
  <div class="info"><i class="ic"></i><div><strong>ADDRESS:</strong><span>465, Lorum Ipsum Dolore,<br>United States</span></div></div>
  <div class="info"><i class="ic"></i><div><strong>PHONE:</strong><span>+1 (888) 888 8888</span></div></div>
  <div class="info"><i class="ic"></i><div><strong>EMAIL:</strong><span>info@nestorbolt.com</span></div></div>
</div>
<div class="fcol" style="left:805px"><h5>Join Newsletter</h5></div>
<div class="abs news"><span>Email Address</span><b>JOIN NOW</b></div>
<div class="abs social fsocial"><span></span><span></span><span></span></div>

<div class="abs bottom-rule"></div>
<div class="abs copy">© 2023 NESTOR BOLT &nbsp;&nbsp;|&nbsp;&nbsp; All Rights Reserved</div>
<div class="abs chat"><svg width="22" height="20" viewBox="0 0 22 20"><path d="M2 2h13v9H7l-4 3v-3H2z" fill="#111"/><path d="M17 6h3v9h-1v3l-4-3H8v-2h9z" fill="#111"/></svg></div>

</body>
</html>
```